Postcard Design: Launch a Spiritual Adventure in Your Church

We are a non-profit coaching, teaching, and consulting Christian ministry. We help churches become more effective in the areas of clarifying their vision, mission, purpose. Our tag line is multiplying hope through healthy churches and must be on the postcard.

We need a postcard design to advertise our ministry to church networks and denominations. We work with all different denominations and Christian church affiliations.

Our core service is called a diagnostic consultation; a very intensive and extensive approach to church health and vitality. It is proven to be a very transformational process for a church. We need a design to communicate our focused mission to help churches become more effective and launch them into a spiritual adventure.

Target Market(s)

Executive Pastors and Executive level Christian Ministry leaders

Industry/Entity Type

Non-Profit

Requirements
Must have
• Our logo, website, tagline, tollfree number

```html
<!DOCTYPE html>
<html lang="en">
<head>
<meta charset="utf-8">
<title>Postcard Back – Harvest Lamp Ministries</title>
<link rel="stylesheet" href="https://fonts.googleapis.com/css2?family=Open+Sans:wdth,wght@75..100,400..800&display=swap">
<style>
  :root {
    --card-bg: #fcefa9;
    --panel-bg: #ebc475;
    --ink: #1d1a14;
    --accent: #c98a3a;
    --star: #d9a24a;
    --rule: #1d1a14;
  }
  * { margin: 0; padding: 0; box-sizing: border-box; }
  html, body { width: 1200px; height: 929px; overflow: hidden; }
  body { background: var(--card-bg); font-family: "Open Sans", Arial, sans-serif; color: var(--ink); }
  .postcard { position: relative; width: 1200px; height: 929px; background: var(--card-bg); overflow: hidden; }

  .benefits-panel {
    position: absolute; left: 0; top: 0; width: 580px; height: 495px;
    background: var(--panel-bg); padding: 46px 20px 0 52px;
  }
  .benefits-title { font-weight: 700; font-size: 21px; line-height: 27px; margin-bottom: 8px; }
  .benefits-list { list-style: none; font-stretch: 75%; font-size: 19.5px; line-height: 27px; }
  .benefits-list li { position: relative; padding-left: 25px; }
  .benefits-list .star { position: absolute; left: 0; top: 6px; width: 15px; height: 15px; }

  .offer { position: absolute; left: 78px; top: 515px; font-size: 17.5px; line-height: 27px; }
  .offer .phone { font-weight: 700; font-size: 22px; }

  .contact { position: absolute; left: 78px; top: 619px; font-size: 20px; line-height: 30px; }
  .contact .org-name { color: var(--accent); font-weight: 700; font-size: 20.5px; }

  .label { position: absolute; font-size: 29px; line-height: 39px; }
  .postage-label { left: 960px; top: 128px; width: 160px; text-align: center; }
  .address-label { left: 644px; top: 392px; font-size: 30px; }
  .barcode-label { left: 576px; top: 822px; }
  .address-line { position: absolute; left: 654px; width: 468px; height: 0; border-top: 1.5px solid var(--rule); }
</style>
</head>
<body>
<main class="postcard">
  <section class="benefits-panel">
    <h2 class="benefits-title">Under God’s blessings, you can expect most<br>or all of the following benefits:</h2>
    <ul class="benefits-list">
      <li><svg class="star" viewBox="0 0 16 16"><path d="M8 0 L9.3 6.7 L16 8 L9.3 9.3 L8 16 L6.7 9.3 L0 8 L6.7 6.7 Z" fill="var(--star)"/></svg>Affirmation of what you are doing right.</li>
      <li><svg class="star" viewBox="0 0 16 16"><path d="M8 0 L9.3 6.7 L16 8 L9.3 9.3 L8 16 L6.7 9.3 L0 8 L6.7 6.7 Z" fill="var(--star)"/></svg>Clear understanding of opportunities that exist for growth,<br>ministry, and service to your community.</li>
      <li><svg class="star" viewBox="0 0 16 16"><path d="M8 0 L9.3 6.7 L16 8 L9.3 9.3 L8 16 L6.7 9.3 L0 8 L6.7 6.7 Z" fill="var(--star)"/></svg>Identification of and strategic approaches for removing roadblocks<br>to congregational vitality and growth.</li>
      <li><svg class="star" viewBox="0 0 16 16"><path d="M8 0 L9.3 6.7 L16 8 L9.3 9.3 L8 16 L6.7 9.3 L0 8 L6.7 6.7 Z" fill="var(--star)"/></svg>A renewed clarity concerning the purpose of the church.</li>
      <li><svg class="star" viewBox="0 0 16 16"><path d="M8 0 L9.3 6.7 L16 8 L9.3 9.3 L8 16 L6.7 9.3 L0 8 L6.7 6.7 Z" fill="var(--star)"/></svg>Among a majority of active members - a significantly increased<br>enthusiasm, involvement, and ownership in the work of the church.</li>
      <li><svg class="star" viewBox="0 0 16 16"><path d="M8 0 L9.3 6.7 L16 8 L9.3 9.3 L8 16 L6.7 9.3 L0 8 L6.7 6.7 Z" fill="var(--star)"/></svg>Increased financial giving - a result of an enhanced vision.</li>
      <li><svg class="star" viewBox="0 0 16 16"><path d="M8 0 L9.3 6.7 L16 8 L9.3 9.3 L8 16 L6.7 9.3 L0 8 L6.7 6.7 Z" fill="var(--star)"/></svg>Increased focus among leadership, promoting greater unity and<br>effectiveness.</li>
      <li><svg class="star" viewBox="0 0 16 16"><path d="M8 0 L9.3 6.7 L16 8 L9.3 9.3 L8 16 L6.7 9.3 L0 8 L6.7 6.7 Z" fill="var(--star)"/></svg>Specific, recommended changes or additions in programming,<br>staffing, facilities, etc.</li>
      <li><svg class="star" viewBox="0 0 16 16"><path d="M8 0 L9.3 6.7 L16 8 L9.3 9.3 L8 16 L6.7 9.3 L0 8 L6.7 6.7 Z" fill="var(--star)"/></svg>New insights for ministry activities.</li>
    </ul>
  </section>

  <p class="offer">
    A Free Information Kit is available with no obligation.<br>
    Cost is based on the size of congregation and staff.<br>
    Call for a price - <span class="phone">800-555-0142</span>
  </p>

  <address class="contact" style="font-style:normal">
    <span class="org-name">HARVEST LAMP MINISTRIES</span><br>
    4870 County Road Nine Millbrook,<br>
    IN 46999 USA<br>
    hello@harvestlamp.org<br>
    www.harvestlamp.org
  </address>

  <div class="label postage-label">Postage<br>Area</div>
  <div class="label address-label">Parents Address Area</div>
  <div class="address-line" style="top:497px"></div>
  <div class="address-line" style="top:589px"></div>
  <div class="address-line" style="top:680px"></div>
  <div class="label barcode-label">Barcode Area</div>
</main>
</body>
</html>
```